TKV Roofing Flyer/Mailer to be used to market to Homeowners

We need to create a flyer than can double as a mailer for our roofing business and possibly be used as a door hanger as well. This flyer will advertise our roofing company in a professional way with pictures as well as clear and precise text about who we are and what we offer. We are open to this flyer being a bi-fold or even a tri-fold. There would need to be an area for address if used as a mailer. A majority of our company information can be found on our website at www.tkvroofing-example.com.

Target Market(s)

Home Owners

Industry/Entity Type

Construction

Colors
0255a3
ffffff

Requirements
Must have
• Professional design, pictures, text with info regarding our company. Website: www.tkvroofing-example.com

```html
<!DOCTYPE html>
<html lang="en">
<head>
<meta charset="utf-8">
<title>TKV Roofing Tri-fold Flyer</title>
<link href="https://fonts.googleapis.com/css2?family=Oswald:wght@500;600;700&family=Open+Sans:wght@400;600;700&family=Cinzel:wght@600&display=swap" rel="stylesheet">
<style>
:root{
  --brand:#0255a3;
  --white:#ffffff;
  --ink:#3a3f47;
  --muted:#6b7380;
  --box:#e4e8ee;
  --tick:#3aa845;
  --bg:#d9dcdf;
}
*{box-sizing:border-box;margin:0;padding:0}
html,body{width:1200px;height:1200px;overflow:hidden;background:var(--bg)}
body{font-family:"Open Sans",Arial,sans-serif;color:var(--ink);position:relative}
.sheet{position:absolute;left:30px;width:1140px;height:575px;background:var(--white);box-shadow:0 4px 14px rgba(0,0,0,.18);overflow:hidden}
.sheet--outside{top:15px}
.sheet--inside{top:610px}
.panel{position:absolute;top:0;width:380px;height:575px}
.panel--1{left:0}.panel--2{left:380px}.panel--3{left:760px}
.fold{position:absolute;top:0;width:1px;height:575px;background:rgba(0,0,0,.08)}
.photo{position:absolute}
.chevron{position:absolute}
.brand{display:flex;align-items:center;gap:8px;font-family:"Open Sans",Arial,sans-serif;font-weight:700;color:var(--brand);white-space:nowrap}
.brand__mark{width:14px;height:14px;background:var(--brand);flex:none}
.brand--lg{font-size:28px}
.brand--md{font-size:20px}
/* outside */
.services__title{position:absolute;left:30px;top:30px;font-family:Oswald,sans-serif;font-weight:600;font-size:17px;color:var(--brand);letter-spacing:.5px}
.services__list{position:absolute;top:62px;list-style:none;font-size:10px;line-height:16.5px;color:var(--ink)}
.services__list li{display:flex;align-items:center;gap:5px}
.services__list--a{left:30px}.services__list--b{left:190px}
.tick{width:10px;height:10px;flex:none}
.offer{position:absolute;width:150px;background:var(--box);border-radius:4px;overflow:hidden;text-align:center}
.offer__head{background:var(--brand);height:24px;display:flex;align-items:center;justify-content:center}
.offer__text{font-size:7.5px;line-height:10px;color:var(--muted);padding:6px 10px 2px}
.offer__name{font-family:Oswald,sans-serif;font-weight:600;font-size:12px;color:var(--brand);padding:2px 0 7px}
.contact{position:absolute;left:60px;top:292px;width:260px;text-align:center;font-size:11px;line-height:14px;color:var(--ink)}
.contact .brand{justify-content:center;margin-bottom:12px}
.contact__row{display:flex;flex-direction:column;align-items:center;margin-bottom:7px}
.contact__row svg{width:13px;height:13px;margin-bottom:2px}
.web{font-size:10px;letter-spacing:2.5px;color:var(--muted)}
.cover__kicker{position:absolute;left:40px;top:348px;font-family:Oswald,sans-serif;font-weight:500;font-size:22px;color:var(--ink)}
.cover__title{position:absolute;left:40px;top:378px;font-family:Oswald,sans-serif;font-weight:700;font-size:38px;color:var(--brand);letter-spacing:.5px}
.cover__copy{position:absolute;left:40px;top:440px;width:300px;font-size:11px;line-height:16px;color:var(--ink)}
.cover__web{position:absolute;left:40px;top:505px;width:300px;text-align:center}
/* inside */
.about{position:absolute;left:28px;top:62px;width:330px;font-size:7.6px;line-height:10.6px;color:var(--ink)}
.about p{text-align:justify;margin-bottom:9px}
.about .bio__name,.bios .bio__name{font-family:Oswald,sans-serif;font-weight:600;font-size:11px;line-height:14px;color:var(--ink);letter-spacing:.3px;margin:0 0 4px;text-align:left}
.bios{position:absolute;left:22px;top:240px;width:335px;font-size:7.6px;line-height:10.6px}
.bios p{margin-bottom:12px;text-align:justify}
.types{position:absolute;left:28px;top:236px;width:330px}
.types__title{font-family:Cinzel,serif;font-weight:600;font-size:15px;color:var(--brand);letter-spacing:.5px;margin-bottom:12px}
.type__name{font-family:Oswald,sans-serif;font-weight:600;font-size:11.5px;line-height:15px;color:var(--ink);letter-spacing:.3px}
.type__text{font-size:7.6px;line-height:10.4px;color:var(--ink);margin-bottom:9px}
.cta{position:absolute;left:150px;top:478px;font-family:Oswald,sans-serif;font-weight:600;color:var(--ink);line-height:24px}
.cta__line1{font-size:20px}
.cta__line2{font-size:20px;display:flex;align-items:center;gap:6px}
.cta__line2 svg{width:16px;height:16px}
.types__web{position:absolute;left:80px;top:545px;width:280px;text-align:center;border-top:1px solid #c9ced6;padding-top:4px}
</style>
</head>
<body>

<section class="sheet sheet--outside">
  <div class="panel panel--1">
    <h2 class="services__title">OUR ROOFING SERVICE</h2>
    <ul class="services__list services__list--a">
      <li><svg class="tick" viewBox="0 0 10 10"><circle cx="5" cy="5" r="5" fill="#3aa845"/><path d="M2.6 5.2l1.6 1.6 3.2-3.4" stroke="#fff" stroke-width="1.3" fill="none"/></svg>Roof Repair</li>
      <li><svg class="tick" viewBox="0 0 10 10"><circle cx="5" cy="5" r="5" fill="#3aa845"/><path d="M2.6 5.2l1.6 1.6 3.2-3.4" stroke="#fff" stroke-width="1.3" fill="none"/></svg>Roof Replacement</li>
      <li><svg class="tick" viewBox="0 0 10 10"><circle cx="5" cy="5" r="5" fill="#3aa845"/><path d="M2.6 5.2l1.6 1.6 3.2-3.4" stroke="#fff" stroke-width="1.3" fill="none"/></svg>Roof Installation</li>
      <li><svg class="tick" viewBox="0 0 10 10"><circle cx="5" cy="5" r="5" fill="#3aa845"/><path d="M2.6 5.2l1.6 1.6 3.2-3.4" stroke="#fff" stroke-width="1.3" fill="none"/></svg>Storm Damage Repair</li>
      <li><svg class="tick" viewBox="0 0 10 10"><circle cx="5" cy="5" r="5" fill="#3aa845"/><path d="M2.6 5.2l1.6 1.6 3.2-3.4" stroke="#fff" stroke-width="1.3" fill="none"/></svg>Roof Inspections</li>
      <li><svg class="tick" viewBox="0 0 10 10"><circle cx="5" cy="5" r="5" fill="#3aa845"/><path d="M2.6 5.2l1.6 1.6 3.2-3.4" stroke="#fff" stroke-width="1.3" fill="none"/></svg>Flat Roofs</li>
      <li><svg class="tick" viewBox="0 0 10 10"><circle cx="5" cy="5" r="5" fill="#3aa845"/><path d="M2.6 5.2l1.6 1.6 3.2-3.4" stroke="#fff" stroke-width="1.3" fill="none"/></svg>Shingle Roofs</li>
      <li><svg class="tick" viewBox="0 0 10 10"><circle cx="5" cy="5" r="5" fill="#3aa845"/><path d="M2.6 5.2l1.6 1.6 3.2-3.4" stroke="#fff" stroke-width="1.3" fill="none"/></svg>Rubber Roofs</li>
      <li><svg class="tick" viewBox="0 0 10 10"><circle cx="5" cy="5" r="5" fill="#3aa845"/><path d="M2.6 5.2l1.6 1.6 3.2-3.4" stroke="#fff" stroke-width="1.3" fill="none"/></svg>Asphalt Roofs</li>
      <li><svg class="tick" viewBox="0 0 10 10"><circle cx="5" cy="5" r="5" fill="#3aa845"/><path d="M2.6 5.2l1.6 1.6 3.2-3.4" stroke="#fff" stroke-width="1.3" fill="none"/></svg>Pitched Roofs</li>
      <li><svg class="tick" viewBox="0 0 10 10"><circle cx="5" cy="5" r="5" fill="#3aa845"/><path d="M2.6 5.2l1.6 1.6 3.2-3.4" stroke="#fff" stroke-width="1.3" fill="none"/></svg>Metal Roofs</li>
      <li><svg class="tick" viewBox="0 0 10 10"><circle cx="5" cy="5" r="5" fill="#3aa845"/><path d="M2.6 5.2l1.6 1.6 3.2-3.4" stroke="#fff" stroke-width="1.3" fill="none"/></svg>Pipe Boots</li>
    </ul>
    <ul class="services__list services__list--b">
      <li><svg class="tick" viewBox="0 0 10 10"><circle cx="5" cy="5" r="5" fill="#3aa845"/><path d="M2.6 5.2l1.6 1.6 3.2-3.4" stroke="#fff" stroke-width="1.3" fill="none"/></svg>Flashings</li>
      <li><svg class="tick" viewBox="0 0 10 10"><circle cx="5" cy="5" r="5" fill="#3aa845"/><path d="M2.6 5.2l1.6 1.6 3.2-3.4" stroke="#fff" stroke-width="1.3" fill="none"/></svg>Siding Repair</li>
      <li><svg class="tick" viewBox="0 0 10 10"><circle cx="5" cy="5" r="5" fill="#3aa845"/><path d="M2.6 5.2l1.6 1.6 3.2-3.4" stroke="#fff" stroke-width="1.3" fill="none"/></svg>Siding Replacement</li>
      <li><svg class="tick" viewBox="0 0 10 10"><circle cx="5" cy="5" r="5" fill="#3aa845"/><path d="M2.6 5.2l1.6 1.6 3.2-3.4" stroke="#fff" stroke-width="1.3" fill="none"/></svg>Siding Installation</li>
      <li><svg class="tick" viewBox="0 0 10 10"><circle cx="5" cy="5" r="5" fill="#3aa845"/><path d="M2.6 5.2l1.6 1.6 3.2-3.4" stroke="#fff" stroke-width="1.3" fill="none"/></svg>Gutter Replacement</li>
      <li><svg class="tick" viewBox="0 0 10 10"><circle cx="5" cy="5" r="5" fill="#3aa845"/><path d="M2.6 5.2l1.6 1.6 3.2-3.4" stroke="#fff" stroke-width="1.3" fill="none"/></svg>Skylights</li>
      <li><svg class="tick" viewBox="0 0 10 10"><circle cx="5" cy="5" r="5" fill="#3aa845"/><path d="M2.6 5.2l1.6 1.6 3.2-3.4" stroke="#fff" stroke-width="1.3" fill="none"/></svg>Ridge Vents</li>
      <li><svg class="tick" viewBox="0 0 10 10"><circle cx="5" cy="5" r="5" fill="#3aa845"/><path d="M2.6 5.2l1.6 1.6 3.2-3.4" stroke="#fff" stroke-width="1.3" fill="none"/></svg>Free Estimates</li>
      <li><svg class="tick" viewBox="0 0 10 10"><circle cx="5" cy="5" r="5" fill="#3aa845"/><path d="M2.6 5.2l1.6 1.6 3.2-3.4" stroke="#fff" stroke-width="1.3" fill="none"/></svg>Free Consultations</li>
      <li><svg class="tick" viewBox="0 0 10 10"><circle cx="5" cy="5" r="5" fill="#3aa845"/><path d="M2.6 5.2l1.6 1.6 3.2-3.4" stroke="#fff" stroke-width="1.3" fill="none"/></svg>2 YR Service Warranties</li>
      <li><svg class="tick" viewBox="0 0 10 10"><circle cx="5" cy="5" r="5" fill="#3aa845"/><path d="M2.6 5.2l1.6 1.6 3.2-3.4" stroke="#fff" stroke-width="1.3" fill="none"/></svg>Emergency Roof Repairs</li>
      <li><svg class="tick" viewBox="0 0 10 10"><circle cx="5" cy="5" r="5" fill="#3aa845"/><path d="M2.6 5.2l1.6 1.6 3.2-3.4" stroke="#fff" stroke-width="1.3" fill="none"/></svg>And More!</li>
    </ul>

    <div class="offer" style="left:30px;top:290px">
      <div class="offer__head"><svg width="14" height="14" viewBox="0 0 14 14"><path d="M2 12l6-6M9 2l3 3-2 2-3-3z" stroke="#fff" stroke-width="1.6" fill="none"/></svg></div>
      <p class="offer__text">We specialize in residential and commercial roofing repairs.</p>
      <p class="offer__name">ROOF REPAIR</p>
    </div>
    <div class="offer" style="left:200px;top:270px">
      <div class="offer__head"><svg width="14" height="14" viewBox="0 0 14 14"><path d="M2 7l5-5 5 5M4 6v6h6V6" stroke="#fff" stroke-width="1.5" fill="none"/></svg></div>
      <p class="offer__text">We provide prompt and professional roof replacement service.</p>
      <p class="offer__name">ROOF REPLACEMENT</p>
    </div>
    <div class="offer" style="left:30px;top:380px">
      <div class="offer__head"><svg width="14" height="14" viewBox="0 0 14 14"><path d="M8 1L3 8h4l-1 5 5-7H7z" fill="#fff"/></svg></div>
      <p class="offer__text">When a storm hits, we provide swift roof repairs and free checkups.</p>
      <p class="offer__name">STORM DAMAGE REPAIR</p>
    </div>
    <div class="offer" style="left:200px;top:360px">
      <div class="offer__head"><svg width="14" height="14" viewBox="0 0 14 14"><rect x="2" y="4" width="10" height="8" rx="1" stroke="#fff" stroke-width="1.4" fill="none"/><path d="M5 4V2h4v2" stroke="#fff" stroke-width="1.4" fill="none"/></svg></div>
      <p class="offer__text">We can help you with your roof insurance claims.</p>
      <p class="offer__name">INSURANCE CLAIMS</p>
    </div>

    <div class="photo" role="img" aria-label="Photo of a brick house under construction with exposed roof framing against a cloudy sky" style="left:0;top:472px;width:380px;height:103px;background:linear-gradient(180deg,#eef3f8 0%,#c9d6e3 30%,#a87a5c 70%,#6e4a33 100%)"></div>
  </div>

  <div class="photo" role="img" aria-label="Photo of a large stone and shingle family home with a green front lawn" style="left:380px;top:75px;width:760px;height:185px;background:linear-gradient(180deg,#dfeaf4 0%,#b9c8d6 30%,#8a7a70 60%,#6f8f5a 100%)"></div>
  <svg class="chevron" width="760" height="70" viewBox="0 0 760 70" style="left:380px;top:220px">
    <path d="M0 0 L190 50 L380 0 L760 0 L760 70 L0 70 Z" fill="#fff"/>
    <path d="M0 4 L190 54 L380 4 L760 4" stroke="#0255a3" stroke-width="4" fill="none"/>
  </svg>

  <div class="panel panel--2">
    <div class="contact">
      <div class="brand brand--md"><span class="brand__mark"></span>TKV Roofing</div>
      <div class="contact__row"><svg viewBox="0 0 14 14"><path d="M3 1l2 3-1.5 1.5a8 8 0 004 4L9 8l3 2-1 3C6 13 1 8 1 3z" fill="#0255a3"/></svg>555-014-2290</div>
      <div class="contact__row"><svg viewBox="0 0 14 14"><rect x="1" y="3" width="12" height="8" stroke="#0255a3" stroke-width="1.4" fill="none"/><path d="M1 3l6 5 6-5" stroke="#0255a3" stroke-width="1.4" fill="none"/></svg>info@tkvroofing-example.com</div>
      <div class="contact__row"><svg viewBox="0 0 14 14"><path d="M7 1a4 4 0 014 4c0 3-4 8-4 8S3 8 3 5a4 4 0 014-4z" fill="#0255a3"/><circle cx="7" cy="5" r="1.5" fill="#fff"/></svg>4810 Cedar Hollow Lane<br>Fishers, IN 46000</div>
      <div class="contact__row"><svg viewBox="0 0 14 14"><circle cx="7" cy="7" r="6" stroke="#0255a3" stroke-width="1.4" fill="none"/><path d="M7 3.5V7l2.5 1.5" stroke="#0255a3" stroke-width="1.4" fill="none"/></svg>Opening Hour<br>Monday - Saturday<br>8:00 am - 8:00 pm</div>
      <p class="web">www.tkvroofing-example.com</p>
    </div>
  </div>

  <div class="panel panel--3">
    <div class="brand brand--lg" style="position:absolute;left:110px;top:22px"><span class="brand__mark"></span>TKV Roofing</div>
    <h2 class="cover__kicker">Residential &amp; Commercial</h2>
    <h1 class="cover__title">ROOFING SERVICES</h1>
    <p class="cover__copy">Our Indianapolis roofing contractors are the skilled professionals to trust for superior service and unparalleled customer support.</p>
    <p class="web cover__web">www.tkvroofing-example.com</p>
  </div>

  <div class="fold" style="left:380px"></div>
  <div class="fold" style="left:760px"></div>
</section>

<section class="sheet sheet--inside">
  <div class="panel panel--1">
    <div class="brand brand--md" style="position:absolute;left:120px;top:25px"><span class="brand__mark"></span>TKV Roofing</div>
    <div class="about">
      <p>The team here at TKV Roofing is a hardworking group of licensed, bonded and insured contractors with more than 25 years of experience. We are a locally owned and operated company dedicated to providing the highest standards of excellence in the roofing and siding service industry here in Indiana. We serve both residential and commercial properties with superior workmanship and unparalleled customer service at an affordable price. We are happy to provide free over-the-phone estimates, but you may also schedule a free in-home consultation for a written quote, anytime. Call our office at 555-014-2290 to speak directly with one of our professional roofing contractors about your exterior home improvement needs.</p>
      <p class="bio__name">DEAN HOLLIS – OWNER</p>
      <p>The team here at TKV Roofing is a hardworking group of licensed, bonded and insured contractors with more than 25 years of experience. We are a locally owned and operated company dedicated to the highest standards in the roofing and siding industry. We serve residential and commercial properties with superior workmanship at an affordable price. Call us anytime for a free in-home consultation and a written quote.</p>
      <p class="bio__name">DEAN HOLLIS – OWNER</p>
      <p>Dean has over 20 years of residential construction and customer service experience. Before starting TKV Roofing, he held a senior management role with one of the largest home builders in the state, where his focus was customer service and satisfaction. This experience makes Dean a leader in the home improvement field. He is married to his wonderful wife, and together they have two kids and love spending quality time with the family.</p>
      <p class="bio__name">GRANT PALMER – OWNER</p>
      <p>Grant is a professional contractor with over 20 years of residential construction experience. Prior to founding TKV Roofing, he held a senior management role with a respected home builder, excelling in sales, operations and service. He and his wife are devoted parents to three children, active in their church and community, and strong believers in old fashioned values of integrity and hard work.</p>
    </div>
    <div class="photo" role="img" aria-label="Faded photo of a stone house entrance" style="left:0;top:490px;width:380px;height:85px;background:linear-gradient(180deg,#e9ebee 0%,#bfc4ca 100%)"></div>
    <svg class="chevron" width="380" height="40" viewBox="0 0 380 40" style="left:0;top:470px">
      <path d="M0 0 L380 0 L380 20 L190 36 L0 20 Z" fill="#fff"/>
      <path d="M0 22 L190 38 L380 22" stroke="#0255a3" stroke-width="4" fill="none"/>
    </svg>
  </div>

  <div class="photo" role="img" aria-label="Photo of a house with red clay tile roofs, skylights and brick chimneys under a blue sky" style="left:380px;top:40px;width:760px;height:175px;background:linear-gradient(180deg,#dce9f5 0%,#b8cfe4 35%,#b5573c 65%,#8c3f2b 100%)"></div>
  <svg class="chevron" width="760" height="60" viewBox="0 0 760 60" style="left:380px;top:175px">
    <path d="M0 8 L190 40 L760 4 L760 60 L0 60 Z" fill="#fff"/>
    <path d="M0 8 L190 40 L760 4" stroke="#0255a3" stroke-width="4" fill="none"/>
  </svg>

  <div class="panel panel--2">
    <div class="bios">
      <p class="bio__name">OWEN CARVER – ACCOUNTING MANAGER</p>
      <p>Owen attended Midland State University in Indianapolis. He has over 25 years of experience in small business accounting, finance and administration for both sales and service organizations, with a special focus on construction industries. He and his wife have been married for 33 years and raised four wonderful children.</p>
      <p class="bio__name">DANA WHITFIELD – ADMINISTRATION</p>
      <p>Dana has an accounting degree from Larkspur College. She has lived in Indianapolis for over 10 years and has been married for 19 years with three wonderful kids. Dana loves spending time with her family and volunteering for local organizations, and she is an invaluable team member here at TKV Roofing.</p>
      <p class="bio__name">LUKE BRANDT – CONTRACTOR</p>
      <p>Luke brings a wealth of varied residential construction and renovation experience to our company. He has spent the past 8 years completing an apprenticeship with a master builder, carpenter and general facilities engineer. This depth of hands-on training makes him a highly qualified member of our team. In his spare time, Luke enjoys time with family and friends and caring for his beloved dogs.</p>
    </div>
  </div>

  <div class="panel panel--3">
    <div class="types">
      <h2 class="types__title">ROOF TYPES WE SPECIALIZE IN</h2>
      <p class="type__name">SHINGLE ROOFING</p>
      <p class="type__text">From TPO and modified bitumen roofing to EPDM, BUR, PVC, SPF and single-ply roofing, our professional contractors are licensed and fully equipped to do it all.</p>
      <p class="type__name">METAL ROOFING</p>
      <p class="type__text">Whether historic standing seam or modern-day steel panels, we have the innovative technologies and quality products to service all metal roofing types.</p>
      <p class="type__name">SHINGLE ROOFING</p>
      <p class="type__text">As one of the most popular roofing types in Indiana, our skilled contractors are highly proficient in shingle roof work for residential and commercial structures.</p>
      <p class="type__name">RUBBER ROOFING</p>
      <p class="type__text">EPDM single-ply membrane roofing is a cost-effective, long-lasting alternative for large roofs, flat roofs, commercial roofs and more.</p>
    </div>
    <div class="cta">
      <p class="cta__line1">Call Today!</p>
      <p class="cta__line2"><svg viewBox="0 0 16 16"><circle cx="8" cy="8" r="7" stroke="#0255a3" stroke-width="1.5" fill="none"/><path d="M5.5 4l1.3 2-1 1a5 5 0 002.2 2.2l1-1 2 1.3-.7 1.8C7.5 11 4.8 8.3 4.5 5z" fill="#0255a3"/></svg>555-014-2290</p>
    </div>
    <p class="web types__web">www.tkvroofing-example.com</p>
  </div>

  <div class="fold" style="left:380px"></div>
  <div class="fold" style="left:760px"></div>
</section>

</body>
</html>
```